Quenby Computers Customer Acquisition Flyer

I need a flyer design for Quenby Computers which is aimed at acquiring new customers. They will be distributed in a letterbox drop and as handouts.

The design should communicate our ability to aid both consumer and small business with all their IT needs and wants, that we have all tools and skills to assist them. It would look modern, professional with a design on the bolder side of the scale.

Very little text to go on flyer, its more about letting people know who we are, wand what we do.

We do:
Computer hardware / software installation and troubleshooting
Custom built computers
Internet installations / WiFi set up
Network installation and consultation
Computer IT Security
Cloud Computing experts
Certified Torvan phone technicians.

not all of that needs to be on flyer, but if is an computer or connected to a computer / network, we can help you.

I have no preference on colours apart from logo which should not be changed.

If anyone require any more information to create a flyer, just ask me, as i am not sure how much information is needed.

Flyer should be in A5 format.

Target Market(s)

consumer and small business (1-50 employees)

Industry/Entity Type

Computer Repair

Requirements
Must have
• Clear easy to read text, graphics that convey us as the professionals we are.
• Logo with tag line, Your local IT specialists
• Contact details:
• Mobile: 0479 612 304
• Email: support@quenbycomputers.com.au
• Web: www.quenbycomputers.com.au
• Be in A5 format
Nice to have
• contact details like mobile to really stand out along with logo.
Should not have
• Go wild, you should not restrict too much the creative people out there.

```html
<!DOCTYPE html>
<html lang="en">
<head>
<meta charset="utf-8">
<title>Quenby Computers – Your Local IT Specialists</title>
<link rel="stylesheet" href="https://fonts.googleapis.com/css2?family=Archivo+Black&family=Libre+Caslon+Text:wght@400&family=Tinos&display=swap">
<style>
  :root {
    --red: #e3262b;
    --red-deep: #c41a20;
    --grey: #cfd0d2;
    --grey-dark: #8a8b8d;
    --ink: #1e1e1e;
    --white: #ffffff;
    --photo-warm: #c9a58c;
    --photo-cool: #6d6f76;
  }
  * { margin: 0; padding: 0; box-sizing: border-box; }
  html, body { width: 849px; height: 1200px; overflow: hidden; background: var(--white); }
  .flyer { position: relative; width: 849px; height: 1200px; overflow: hidden; background: var(--white); }
  .flyer__shapes { position: absolute; inset: 0; width: 849px; height: 1200px; }
  .brand {
    position: absolute; left: 120px; top: 40px;
    display: flex; align-items: center; gap: 18px;
    font-family: "Archivo Black", "Arial Black", sans-serif;
    font-size: 58px; line-height: 1; color: var(--red);
    text-transform: uppercase; letter-spacing: -1px;
  }
  .brand__dot { width: 30px; height: 30px; border-radius: 50%; background: var(--red); }
  .hero-photo {
    position: absolute; left: 269px; top: 240px; width: 580px; height: 425px;
    background: linear-gradient(135deg, var(--photo-cool) 0%, #a9978d 45%, var(--photo-warm) 75%, #e9dfd8 100%);
  }
  .tagline {
    position: absolute; left: 150px; top: 470px;
    font-family: "Archivo Black", "Arial Black", sans-serif;
    font-size: 88px; line-height: 0.98; color: #b9babc;
    text-shadow: 3px 3px 0 #3a3a3a, -1px -1px 0 #3a3a3a, 1px -1px 0 #3a3a3a, -1px 1px 0 #3a3a3a;
    letter-spacing: -2px;
  }
  .tagline span { display: block; }
  .tagline__second { margin-left: -20px; }
  .services {
    position: absolute; left: 0; right: 0; top: 725px;
    list-style: none; text-align: center;
    font-family: "Libre Caslon Text", "Times New Roman", serif;
    font-variant: small-caps; font-size: 29px; letter-spacing: 1px; color: var(--ink);
  }
  .services li { line-height: 51px; }
  .contact {
    position: absolute; left: 0; right: 0; top: 1032px;
    text-align: center; font-family: "Tinos", "Times New Roman", serif;
    font-size: 22px; line-height: 33px; color: var(--ink); font-style: normal;
  }
</style>
</head>
<body>
<main class="flyer">
  <svg class="flyer__shapes" viewBox="0 0 849 1200" aria-hidden="true">
    <path d="M0 0 H849 V250 H269 V665 C170 640 70 600 0 560 Z" fill="var(--red)"/>
    <path d="M0 600 C90 650 190 690 300 700 C180 720 80 700 0 660 Z" fill="var(--grey)"/>
    <path d="M60 160 C200 60 520 40 760 120 C560 100 300 120 110 210 Z" fill="var(--white)"/>
    <path d="M90 30 C300 10 560 20 720 60 L700 170 C520 150 300 150 100 175 Z" fill="var(--white)"/>
    <path d="M849 930 C760 1040 700 1120 650 1200 H849 Z" fill="var(--grey)"/>
    <path d="M849 1010 C800 1080 760 1140 735 1200 H849 Z" fill="var(--red)"/>
  </svg>

  <div class="brand">
    <span class="brand__name">Quenby Computers</span>
    <span class="brand__dot"></span>
  </div>

  <div class="hero-photo" role="img" aria-label="Photo of hands typing on a laptop keyboard"></div>

  <h1 class="tagline">
    <span class="tagline__first">Your Local</span>
    <span class="tagline__second">IT specialists</span>
  </h1>

  <ul class="services">
    <li>Computer hardware / software installations</li>
    <li>Internet installations/WiFi setup</li>
    <li>Network installations consultation</li>
    <li>Computer IT security</li>
    <li>Cloud computing experts</li>
    <li>Certified Torvan phone technicians</li>
  </ul>

  <address class="contact">
    Contact<br>
    Mobile: 0479 612 304<br>
    Email: support@quenbycomputers.com.au<br>
    Web: www.quenbycomputers.com.au
  </address>
</main>
</body>
</html>
```